KORN Tax
Keystone Options and Revenue Navigators
KORN Tax  - Financial Services
Creative Brief
Professional
Tobias Whitlock, CPA CGA
President & CEO
47 Pellam Street Suite 2060 Harborview Court Dartmouth, NS B2C 7K9
rtw@korn.ca
www.korn.ca

```html
<!DOCTYPE html>
<html lang="en">
<head>
<meta charset="utf-8">
<title>KORN Tax Stationery</title>
<link href="https://fonts.googleapis.com/css2?family=Cinzel:wght@600&family=Open+Sans:wght@400;600&display=swap" rel="stylesheet">
<style>
  :root{
    --navy:#16357a;
    --blue:#2a72db;
    --ink:#3a3f4a;
    --muted:#7a808c;
    --paper:#ffffff;
    --backdrop:#eceef1;
  }
  *{box-sizing:border-box;margin:0;padding:0}
  html,body{width:1200px;height:937px;overflow:hidden;background:var(--backdrop)}
  body{position:relative;font-family:"Open Sans",sans-serif;color:var(--ink)}
  .sheet{position:absolute;background:var(--paper);overflow:hidden}
  .swoosh{position:absolute;inset:0;width:100%;height:100%}
  .brand{font-family:"Cinzel",serif;font-weight:600;color:var(--navy);display:flex;align-items:center;gap:6px;white-space:nowrap}
  .brand-dot{display:inline-block;background:var(--navy);border-radius:50%}
  .tagline{font-family:"Cinzel",serif;font-weight:600;color:var(--navy);white-space:nowrap}

  /* letterhead */
  .letterhead{left:182px;top:71px;width:390px;height:541px}
  .letterhead .brand{position:absolute;left:26px;top:30px;font-size:17px}
  .letterhead .brand-dot{width:9px;height:9px}
  .letter-body{position:absolute;left:26px;top:92px;width:290px;font-size:5.2px;line-height:1.6;color:var(--muted)}
  .letter-body p{margin-bottom:9px}
  .signature-line{width:40px;height:12px;border-bottom:1px solid var(--ink);margin:6px 0 4px}
  .letter-contact{position:absolute;right:12px;bottom:46px;width:70px;text-align:right;color:#fff;font-size:4.6px;line-height:1.6}

  /* folder */
  .folder{left:633px;top:38px;width:410px;height:574px}
  .folder .lockup{position:absolute;left:18px;width:300px;top:236px;text-align:center}
  .folder .brand{justify-content:center;font-size:32px;gap:9px}
  .folder .brand-dot{width:15px;height:15px}
  .folder .tagline{font-size:8.5px;margin-top:10px;letter-spacing:.2px}
  .folder-web{position:absolute;right:30px;bottom:26px;color:#fff;font-size:10px;letter-spacing:1.2px}

  /* business cards */
  .card-front{left:43px;top:663px;width:200px;height:91px}
  .card-front .brand{position:absolute;left:10px;top:20px;font-size:11px}
  .card-front .brand-dot{width:6px;height:6px}
  .card-details{position:absolute;left:112px;top:14px;font-size:4.4px;line-height:1.6;color:var(--muted)}
  .card-details .name{color:var(--navy);font-weight:600;font-size:5.4px}
  .card-back{left:43px;top:772px;width:200px;height:94px}
  .card-back .brand{position:absolute;left:12px;top:40px;font-size:12px}
  .card-back .brand-dot{width:6px;height:6px}

  /* envelopes */
  .envelope-front{left:266px;top:663px;width:430px;height:218px}
  .envelope-front .brand{position:absolute;left:22px;top:26px;font-size:20px}
  .envelope-front .brand-dot{width:10px;height:10px}
  .envelope-front .return{position:absolute;left:24px;top:56px;font-size:5px;line-height:1.5;color:var(--muted);width:140px}
  .envelope-back{left:739px;top:663px;width:426px;height:218px}
  .envelope-web{position:absolute;right:24px;top:22px;color:#fff;font-size:9px;letter-spacing:1px}
</style>
</head>
<body>

<section class="sheet letterhead">
  <svg class="swoosh" viewBox="0 0 390 541" preserveAspectRatio="none" aria-hidden="true">
    <path d="M344,0 C332,150 340,360 215,541 L230,541 C350,350 340,150 352,0 Z" fill="var(--blue)"/>
    <path d="M390,0 L352,0 C340,150 350,350 230,541 L390,541 Z" fill="var(--navy)"/>
  </svg>
  <div class="brand"><span class="brand-dot"></span>KORN Tax</div>
  <div class="letter-body">
    <p>July 4, 2024</p>
    <p>Mr. Alan Reed<br>12 Elm Lane<br>Halifax, NS</p>
    <p>Dear Mr. Reed,</p>
    <p>Thank you for choosing our firm for your annual tax review. We have reviewed the documents you provided and prepared a summary of the filing options available to you this year, along with the deadlines that apply.</p>
    <p>Please contact our office to book a meeting at a time that suits you.</p>
    <p>We look forward to helping you plan ahead and keep more of what you earn. Our team is ready to answer any questions about your return, credits and next steps.</p>
    <p>Sincerely,</p>
    <div class="signature-line"></div>
    <p>Tobias Whitlock, CPA CGA<br>President &amp; CEO</p>
  </div>
  <div class="letter-contact">
    47 Pellam Street Suite 2060<br>Harborview Court<br>Dartmouth, NS B2C 7K9<br>Tel 902 555 0147<br>rtw@korn.ca<br>www.korn.ca
  </div>
</section>

<section class="sheet folder">
  <svg class="swoosh" viewBox="0 0 410 574" preserveAspectRatio="none" aria-hidden="true">
    <path d="M322,0 C372,200 335,420 30,574 L50,574 C348,425 385,200 334,0 Z" fill="var(--blue)"/>
    <path d="M410,0 L334,0 C385,200 348,425 50,574 L410,574 Z" fill="var(--navy)"/>
  </svg>
  <div class="lockup">
    <div class="brand"><span class="brand-dot"></span>KORN Tax</div>
    <div class="tagline">Keystone Options and Revenue Navigators</div>
  </div>
  <div class="folder-web">www.korn.ca</div>
</section>

<section class="sheet card-front">
  <svg class="swoosh" viewBox="0 0 200 91" preserveAspectRatio="none" aria-hidden="true">
    <path d="M200,50 C160,72 130,84 94,91 L100,91 C135,85 165,74 200,56 Z" fill="var(--blue)"/>
    <path d="M200,56 C165,74 135,85 100,91 L200,91 Z" fill="var(--navy)"/>
  </svg>
  <div class="brand"><span class="brand-dot"></span>KORN Tax</div>
  <div class="card-details">
    <div class="name">Tobias Whitlock, CPA CGA</div>
    President &amp; CEO<br>Tel 902 555 0147<br>rtw@korn.ca<br>www.korn.ca
  </div>
</section>

<section class="sheet card-back">
  <svg class="swoosh" viewBox="0 0 200 94" preserveAspectRatio="none" aria-hidden="true">
    <path d="M200,58 C165,76 135,88 94,94 L100,94 C140,88 170,78 200,64 Z" fill="var(--blue)"/>
    <path d="M200,64 C170,78 140,88 100,94 L200,94 Z" fill="var(--navy)"/>
  </svg>
  <div class="brand"><span class="brand-dot"></span>KORN Tax</div>
</section>

<section class="sheet envelope-front">
  <svg class="swoosh" viewBox="0 0 430 218" preserveAspectRatio="none" aria-hidden="true">
    <path d="M430,100 C380,165 320,203 240,218 L252,218 C325,204 385,172 430,112 Z" fill="var(--blue)"/>
    <path d="M430,112 C385,172 325,204 252,218 L430,218 Z" fill="var(--navy)"/>
  </svg>
  <div class="brand"><span class="brand-dot"></span>KORN Tax</div>
  <div class="return">47 Pellam Street Suite 2060 Harborview Court Dartmouth, NS B2C 7K9</div>
</section>

<section class="sheet envelope-back">
  <svg class="swoosh" viewBox="0 0 426 218" preserveAspectRatio="none" aria-hidden="true">
    <path d="M0,76 C90,92 160,102 213,118 C260,102 330,92 426,76 L426,70 C330,86 260,96 213,110 C160,96 90,86 0,70 Z" fill="var(--blue)"/>
    <path d="M0,0 L426,0 L426,70 C330,86 260,96 213,110 C160,96 90,86 0,70 Z" fill="var(--navy)"/>
  </svg>
  <div class="envelope-web">www.korn.ca</div>
</section>

</body>
</html>
```